Street Sign Project - Attract Customers

We need a street sign designed to display out the front of the building. It design will need to be 1800mm wide x 900mm high. We need to show potential customers where we are inviting. Some of the attachments are for inspiration. The sign will be printed on a sheet of aluminum. if you have a good look at our web site which is www.pk-r.com.au you should get a good feeling about the company and what we do.

Target Market(s)

Construction companies, landscaping and civil earth moving companies who may drive past our business

Industry/Entity Type

Building

Font styles to use
Sans Serif

Colors
ffffff
3277b5
000000

Requirements
Must have
• Company logo must be the main focus point
• The number "54" on the sign to show street number (300mm high)
• phone number - (02) 9418 3065
• web address - www.pk-r.com.au
• I have loaded pictures i would like to see used in the sign
Nice to have
• Banner picture as attached
Should not have
• Bright colours. Please use our blue colour where possible

```html
<!DOCTYPE html>
<html lang="en">
<head>
<meta charset="utf-8">
<title>Parkline Rigging &amp; Lifting – Street Sign</title>
<link href="https://fonts.googleapis.com/css2?family=Archivo+Black&family=Arimo:wght@700&family=Roboto+Condensed:wght@700&display=swap" rel="stylesheet">
<style>
  :root {
    --sign-blue: #2c96ea;
    --contact-blue: #1f98d9;
    --white: #ffffff;
    --black: #111111;
    --backdrop: #d6d6d6;
  }
  * { box-sizing: border-box; margin: 0; padding: 0; }
  html, body {
    width: 1200px;
    height: 686px;
    overflow: hidden;
    background: var(--backdrop);
  }
  .sign {
    position: absolute;
    left: 0;
    top: 43px;
    width: 1200px;
    height: 600px;
    background: var(--white);
    overflow: hidden;
  }
  .company-name {
    position: absolute;
    left: 34px;
    top: 62px;
    font-family: "Archivo Black", "Arial Black", sans-serif;
    font-size: 92px;
    line-height: 1.2;
    color: var(--sign-blue);
    letter-spacing: 1px;
    white-space: nowrap;
  }
  .company-name span { display: block; }
  .street-number {
    position: absolute;
    left: 886px;
    top: 0;
    width: 314px;
    height: 248px;
  }
  .street-number svg { position: absolute; inset: 0; }
  .street-number .digits {
    position: absolute;
    left: 30px;
    right: 4px;
    top: 0;
    height: 240px;
    display: flex;
    align-items: center;
    justify-content: center;
    font-family: "Arimo", Arial, sans-serif;
    font-weight: 700;
    font-size: 236px;
    line-height: 1;
    color: var(--white);
    letter-spacing: -6px;
    white-space: nowrap;
  }
  .contact {
    position: absolute;
    left: 870px;
    width: 330px;
    text-align: center;
    font-family: "Roboto Condensed", "Arial Narrow", sans-serif;
    font-weight: 700;
    color: var(--contact-blue);
    white-space: nowrap;
  }
  .contact-phone { top: 284px; font-size: 50px; line-height: 1; }
  .contact-web { top: 356px; font-size: 40px; line-height: 1; }
  .photo-band {
    position: absolute;
    left: 0;
    top: 422px;
    width: 1200px;
    height: 178px;
    background: var(--sign-blue);
  }
  .photo {
    position: absolute;
    top: 15px;
    width: 185px;
    height: 146px;
    border-radius: 4px;
  }
  .photo-1 { left: 14px;  background: linear-gradient(180deg, #6b7a5a 0%, #a89a88 45%, #c9c2b8 100%); }
  .photo-2 { left: 211px; background: linear-gradient(180deg, #9fb6c4 0%, #6f8fa0 50%, #b8c2c4 100%); }
  .photo-3 { left: 409px; background: linear-gradient(180deg, #c8d2da 0%, #8a7a70 50%, #5a6a90 100%); }
  .photo-4 { left: 607px; background: linear-gradient(180deg, #aebfd8 0%, #a04a3a 45%, #d8d0c4 100%); }
  .photo-5 { left: 805px; background: linear-gradient(180deg, #c4ccd4 0%, #b8aa90 50%, #6a7078 100%); }
  .photo-6 { left: 1002px; background: linear-gradient(180deg, #d8c8e0 0%, #b8c4d4 45%, #8a98aa 100%); }
</style>
</head>
<body>
  <main class="sign">
    <h1 class="company-name">
      <span>PARKLINE</span>
      <span>RIGGING &amp;</span>
      <span>LIFTING</span>
    </h1>

    <div class="street-number">
      <svg viewBox="0 0 314 248" width="314" height="248" aria-hidden="true">
        <polygon points="26,0 314,0 314,248 28,248 0,128" fill="var(--black)"/>
        <polygon points="36,0 314,0 314,240 37,240 12,128" fill="var(--sign-blue)"/>
      </svg>
      <div class="digits">54</div>
    </div>

    <p class="contact contact-phone">(02) 9418 3065</p>
    <p class="contact contact-web">www.pk-r.com.au</p>

    <section class="photo-band">
      <div class="photo photo-1" role="img" aria-label="Conveyor carrying rubble out of a demolition site"></div>
      <div class="photo photo-2" role="img" aria-label="Goods hoist installed beside a building site"></div>
      <div class="photo photo-3" role="img" aria-label="Material hoist with basket mounted on scaffolding"></div>
      <div class="photo photo-4" role="img" aria-label="Ladder hoist lifting materials onto a tiled roof"></div>
      <div class="photo photo-5" role="img" aria-label="Belt conveyor feeding materials up to scaffolding"></div>
      <div class="photo photo-6" role="img" aria-label="Blue rubbish chute running down a multi-storey building"></div>
    </section>
  </main>
</body>
</html>
```